Tellwick Asset Management - Corporate Letter Head Project

Looking for a classy design based on our current logo. Please find current logo source file in files. With our color scheme.

Target Market(s)

We're an investment firm, the letterhead needs to look professional and attractive to clients.

Industry/Entity Type

Hedgefund

Colors
0054AA
0677BA
7BADD7
CADEEF
E8F1F8

Requirements
Must have
• Our logo, address, phone number, and email

```html
<!DOCTYPE html>
<html lang="en">
<head>
<meta charset="utf-8">
<title>Tellwick Asset Management – Letterhead</title>
<link href="https://fonts.googleapis.com/css2?family=Arimo:wght@400&display=swap" rel="stylesheet">
<style>
  :root {
    --paper: #f5f3f4;
    --navy: #13294a;
    --ink: #3a3a3a;
    --ink-soft: #4a4a4a;
    --sig: #2a2f3a;
    --white: #ffffff;
  }
  * { margin: 0; padding: 0; box-sizing: border-box; }
  html, body { width: 935px; height: 1200px; overflow: hidden; }
  body {
    background: var(--paper);
    font-family: "Arimo", Arial, sans-serif;
    color: var(--ink);
    position: relative;
  }
  .brand-block {
    position: absolute; left: 619px; top: 0; width: 254px; height: 234px;
    background: var(--navy);
    display: flex; flex-direction: column; align-items: center; justify-content: center;
    gap: 14px;
  }
  .brand-square { width: 62px; height: 62px; border: 2px solid var(--white); }
  .brand-name {
    color: var(--white); font-size: 19px; text-align: center;
    letter-spacing: 1.5px; line-height: 1.35; text-transform: uppercase;
  }
  .greeting {
    position: absolute; left: 93px; top: 308px;
    font-size: 22px; color: var(--ink-soft);
  }
  .letter-body {
    position: absolute; left: 93px; top: 378px; width: 755px;
    font-size: 14px; line-height: 20.5px; text-align: justify; hyphens: auto;
  }
  .letter-body p + p { margin-top: 20px; }
  .closing { position: absolute; left: 93px; top: 830px; font-size: 13px; }
  .signature {
    position: absolute; left: 89px; top: 862px; width: 124px; height: 40px;
    background: linear-gradient(90deg, rgba(42,47,58,0.15), rgba(42,47,58,0.05));
  }
  .signer { position: absolute; left: 97px; top: 926px; }
  .signer-name { font-size: 18px; color: var(--ink-soft); }
  .signer-title { font-size: 14px; margin-top: 4px; }
  .contact {
    position: absolute; right: 94px; top: 1077px;
    font-size: 13.5px; line-height: 17px; text-align: right; color: #222;
  }
  .contact-lines { margin-top: 11px; }
  .contact-row { display: flex; justify-content: flex-end; align-items: center; gap: 6px; }
  .contact-row svg { width: 11px; height: 11px; fill: var(--navy); }
  .footer-band {
    position: absolute; left: 619px; top: 1187px; width: 254px; height: 13px;
    background: var(--navy);
  }
</style>
</head>
<body>
  <header class="brand-block">
    <div class="brand-square"></div>
    <div class="brand-name">Tellwick Asset<br>Management</div>
  </header>

  <div class="greeting">Dear Mr. Harlow,</div>

  <main class="letter-body">
    <p>Lorem ipsum dolor sit amet, consectetur adipiscing elit. Donec orci purus, luctus vitae dignissim eu, iaculis sed purus. Vivamus faucibus, ipsum nec aliquet viverra, leo mauris condimentum ligula, sit amet sagittis enim ligula quis arcu. Nam egestas tortor id nisi porttitor mattis. In tortor ante, ultricies in suscipit a, tempus non massa. Vivamus et auctor mi. Fusce vel massa nulla. Phasellus nec eros mauris, et scelerisque orci.</p>
    <p>Donec malesuada orci vitae nulla accumsan porta a id massa. Quisque accumsan iaculis magna sit amet fringilla. Maecenas consequat, magna eget tincidunt semper, odio nibh rutrum mi, id feugiat ante nisi eu risus. Vestibulum nunc orci, rhoncus a placerat in, ultricies in mi. Cras mattis varius eros, vel fringilla nisi suscipit eget. Quisque scelerisque sagittis nulla at porttitor.</p>
    <p>Sed id augue vitae urna euismod commodo aliquet a quam. Pellentesque arcu velit, cursus et malesuada ut, consequat et diam. Nullam erat sem, rhoncus id ullamcorper vitae, rhoncus et arcu. In ultricies ultricies nulla, ut rutrum nisi iaculis at. Donec eu magna a metus ornare faucibus. Fusce aliquet faucibus ultricies. Morbi semper, est id tincidunt gravida, sem arcu adipiscing lacus, ac bibendum nulla leo eu purus. Quisque nec diam sed risus consectetur a ccumsan quis quis nibh. Vestibulum id purus lorem.</p>
    <p>It is a long established fact that a reader will be distracted by the readable content of a page when looking at its layout. The point of using Lorem Ipsum is that it has a more-or-less normal distribution of letters, as opposed to using 'Content here, content here', making it look like readable English. Many desktop publishing packages</p>
  </main>

  <div class="closing">Sincerely,</div>
  <div class="signature" role="img" aria-label="Handwritten signature of Peter Harlow"></div>
  <div class="signer">
    <div class="signer-name">Peter Harlow</div>
    <div class="signer-title">CEO/ Founder</div>
  </div>

  <footer class="contact">
    <address style="font-style:normal">
      2184 Maple Ridge Ct<br>210B Lakeview<br>IN 46390
    </address>
    <div class="contact-lines">
      <div class="contact-row">5550142288
        <svg viewBox="0 0 24 24" aria-hidden="true"><path d="M6.6 10.8a15.2 15.2 0 0 0 6.6 6.6l2.2-2.2c.3-.3.7-.4 1-.2 1.1.4 2.3.6 3.6.6.6 0 1 .4 1 1V20c0 .6-.4 1-1 1A17 17 0 0 1 3 4c0-.6.4-1 1-1h3.5c.6 0 1 .4 1 1 0 1.3.2 2.5.6 3.6.1.3 0 .7-.2 1z"/></svg>
      </div>
      <div class="contact-row">info@TellwickAsset.com
        <svg viewBox="0 0 24 24" aria-hidden="true"><path d="M2 5h20v14H2z M3 6l9 7 9-7" fill="var(--navy)"/><path d="M3.5 6.5l8.5 6.5 8.5-6.5" stroke="#fff" stroke-width="1.6" fill="none"/></svg>
      </div>
    </div>
  </footer>

  <div class="footer-band"></div>
</body>
</html>
```